Building company buisness cards

We are looking for a sharp modern new look for our business cards.We are a New Zealand based company that specialises in house and land packages.We have attached a photo of the current logo and would like to see if it can be improved somehow if needed.We are open to any colours but we have chosen Black and White at this stage. Feel free to change the font and make the logo smarter looking.Play with the colours and see what looks best.We want a card that looks so good know one will want to throw it away!

Target Market(s)

Building profesonals, home buyers

Industry/Entity Type

Building

Contact Information for Business Card

Derek Haskins
0274930268
derekh@stonerange.co.nz

Font styles to use
Serif
Sans Serif

Colors

Designer to choose colors to be used in the design.

Requirements
Must have
• Just the logo on one side and details on the other
• Clean simple looking card
Nice to have
• Round corners and detail like raised or spot UV
• Something that stands out
Should not have
• To title needed, Director etc

```html
<!DOCTYPE html>
<html lang="en">
<head>
<meta charset="utf-8">
<title>Stonerange Business Card</title>
<link rel="stylesheet" href="https://fonts.googleapis.com/css2?family=Montserrat:wght@500;600;700&display=swap">
<style>
  :root {
    --stage: #1d1d1d;
    --card-black: #151515;
    --card-white: #ffffff;
    --band: #1a1a1a;
    --silver: #c4c4c4;
    --ink: #111111;
    --band-text: #b8b8b8;
    --card-w: 600px;
    --card-h: 343px;
    --radius: 18px;
  }
  * { box-sizing: border-box; margin: 0; padding: 0; }
  html, body {
    width: 1200px;
    height: 900px;
    overflow: hidden;
    background: var(--stage);
    font-family: "Montserrat", sans-serif;
  }
  .stage {
    width: 1200px;
    height: 900px;
    display: flex;
    flex-direction: column;
    align-items: center;
    justify-content: center;
    gap: 64px;
  }
  .card {
    width: var(--card-w);
    height: var(--card-h);
    border-radius: var(--radius);
    overflow: hidden;
    position: relative;
  }
  .card-front {
    background: var(--card-black);
    display: flex;
    align-items: center;
    justify-content: center;
  }
  .brand {
    display: flex;
    align-items: center;
    gap: 12px;
  }
  .brand-name {
    font-family: "Montserrat", sans-serif;
    font-weight: 600;
    font-size: 44px;
    letter-spacing: 0.5px;
    color: var(--silver);
  }
  .brand-circle {
    width: 38px;
    height: 38px;
    border: 2px solid var(--silver);
    border-radius: 50%;
  }
  .card-back {
    background: var(--card-white);
  }
  .identity {
    position: absolute;
    top: 58px;
    left: 0;
    right: 0;
    display: flex;
    flex-direction: column;
    align-items: center;
  }
  .identity-circle {
    width: 50px;
    height: 50px;
    border: 2.5px solid var(--ink);
    border-radius: 50%;
  }
  .person-name {
    margin-top: 18px;
    font-weight: 700;
    font-size: 30px;
    color: var(--ink);
    letter-spacing: 0.3px;
  }
  .contact-band {
    position: absolute;
    top: 210px;
    left: 0;
    right: 0;
    height: 70px;
    background: var(--band);
    display: flex;
    align-items: center;
    justify-content: center;
    gap: 48px;
  }
  .contact-item {
    display: flex;
    align-items: center;
    gap: 8px;
    font-weight: 500;
    font-size: 14px;
    color: var(--band-text);
    letter-spacing: 0.3px;
  }
  .contact-item svg { width: 14px; height: 14px; fill: var(--band-text); }
</style>
</head>
<body>
  <main class="stage">
    <section class="card card-front" aria-label="Card front">
      <div class="brand">
        <span class="brand-name">Stonerange</span>
        <span class="brand-circle"></span>
      </div>
    </section>

    <section class="card card-back" aria-label="Card back">
      <div class="identity">
        <span class="identity-circle"></span>
        <h1 class="person-name">Derek Haskins</h1>
      </div>
      <div class="contact-band">
        <span class="contact-item">
          <svg viewBox="0 0 24 24" aria-hidden="true"><path d="M6.6 10.8c1.4 2.8 3.8 5.1 6.6 6.6l2.2-2.2c.3-.3.7-.4 1-.2 1.1.4 2.3.6 3.6.6.6 0 1 .4 1 1V20c0 .6-.4 1-1 1C10.6 21 3 13.4 3 4c0-.6.4-1 1-1h3.5c.6 0 1 .4 1 1 0 1.3.2 2.5.6 3.6.1.3 0 .7-.2 1z"/></svg>
          027 493 0268
        </span>
        <span class="contact-item">
          <svg viewBox="0 0 24 24" aria-hidden="true"><path d="M2 5h20v14H2z M3.5 6.5 12 13l8.5-6.5" fill="none" stroke="#b8b8b8" stroke-width="1.8"/></svg>
          derekh@stonerange.co.nz
        </span>
      </div>
    </section>
  </main>
</body>
</html>
```